Telecommunications/Power civil contractor needs business card design

Were a new telecommunications/power underground civil contractor that is looking for a new business card design. Our company colours are silver or grey and orange. Feel free to use the white background logo or the black background logo.

Target Market(s)

Local contractors, utility companies, private sector mining/energy companies, developers.

Industry/Entity Type

Telecommunications

Contact Information for Business Card

Each card will need the following info:
Persons name:
Title:
E-mail:
Phone number:
Shop Address:
Mailing Address:

Requirements
Must have
• Each card will need the following info:
• Persons name:
• Title:
• E-mail:
• Phone number:
• Shop Address:
• Mailing Address:

```html
<!DOCTYPE html>
<html lang="en">
<head>
<meta charset="utf-8">
<title>Dig Line Contracting Inc – Business Card</title>
<link rel="stylesheet" href="https://fonts.googleapis.com/css2?family=Roboto:wght@400;700&display=swap">
<style>
  :root {
    --orange: #f05a22;
    --grey: #7a7a7c;
    --grey-dark: #4a4a4c;
    --ink: #3a3a3a;
    --card-white: #ffffff;
    --card-black: #111112;
    --backdrop: #2b2b2d;
  }
  * { box-sizing: border-box; margin: 0; padding: 0; }
  html, body { width: 1200px; height: 900px; overflow: hidden; }
  body {
    background: var(--backdrop);
    font-family: "Roboto", Arial, sans-serif;
    position: relative;
  }
  .card {
    position: absolute;
    width: 640px;
    height: 366px;
    border-radius: 3px;
    overflow: hidden;
  }
  .card--front { left: 80px; top: 60px; background: var(--card-white); }
  .card--back { left: 480px; top: 474px; background: var(--card-black); }

  .card__art { position: absolute; inset: 0; }

  .brand {
    position: absolute;
    display: flex;
    align-items: center;
    gap: 14px;
    color: var(--orange);
    font-weight: 700;
    text-transform: uppercase;
    line-height: 1.05;
  }
  .brand__dot {
    border-radius: 50%;
    background: var(--orange);
    flex: none;
  }
  .card--front .brand { left: 40px; top: 56px; font-size: 24px; letter-spacing: 0.5px; }
  .card--front .brand__dot { width: 58px; height: 58px; }
  .brand__sub { display: block; font-size: 0.62em; letter-spacing: 1.5px; }

  .card--back .brand {
    left: 50%; top: 50%;
    transform: translate(-50%, -50%);
    flex-direction: column;
    text-align: center;
    font-size: 40px;
    letter-spacing: 1px;
    gap: 18px;
  }
  .card--back .brand__dot { width: 96px; height: 96px; }

  .person {
    position: absolute;
    right: 40px; top: 40px;
    text-align: right;
    width: 230px;
  }
  .person__name { color: var(--orange); font-weight: 700; font-size: 17px; }
  .person__title { color: var(--ink); font-size: 15px; margin-top: 4px; padding-bottom: 9px; border-bottom: 2px solid var(--orange); }

  .contact {
    position: absolute;
    right: 40px; top: 124px;
    list-style: none;
    text-align: right;
    color: var(--ink);
    font-size: 15px;
    line-height: 26px;
  }
  .contact__item { display: flex; justify-content: flex-end; align-items: center; gap: 8px; }
  .contact__icon { width: 14px; height: 14px; fill: var(--orange); flex: none; }

  .address {
    position: absolute;
    left: 40px; top: 236px;
    color: var(--ink);
    font-size: 15px;
    line-height: 24px;
    font-style: normal;
  }
</style>
</head>
<body>

<section class="card card--front" aria-label="Business card front">
  <svg class="card__art" width="640" height="366" viewBox="0 0 640 366" aria-hidden="true">
    <line x1="44" y1="214" x2="600" y2="214" stroke="var(--grey-dark)" stroke-width="1.5"/>
    <circle cx="44" cy="214" r="4" fill="var(--grey-dark)"/>
    <path d="M360 330 C380 300 395 292 430 292 L640 292 L640 330 Z" fill="var(--orange)"/>
    <line x1="0" y1="338" x2="640" y2="338" stroke="var(--grey)" stroke-width="4"/>
    <line x1="0" y1="348" x2="640" y2="348" stroke="var(--orange)" stroke-width="3"/>
  </svg>

  <div class="brand">
    <span class="brand__dot"></span>
    <span>Dig Line<span class="brand__sub">Contracting Inc</span></span>
  </div>

  <div class="person">
    <p class="person__name">Morgan Hale</p>
    <p class="person__title">Managing Director</p>
  </div>

  <ul class="contact">
    <li class="contact__item">555.201.7788
      <svg class="contact__icon" viewBox="0 0 24 24" aria-hidden="true"><path d="M6.6 10.8a15.1 15.1 0 0 0 6.6 6.6l2.2-2.2a1 1 0 0 1 1-.25 11.4 11.4 0 0 0 3.6.57 1 1 0 0 1 1 1V20a1 1 0 0 1-1 1A17 17 0 0 1 3 4a1 1 0 0 1 1-1h3.5a1 1 0 0 1 1 1c0 1.25.2 2.45.57 3.57a1 1 0 0 1-.25 1z"/></svg>
    </li>
    <li class="contact__item">info@diglinecontracting.com
      <svg class="contact__icon" viewBox="0 0 24 24" aria-hidden="true"><path d="M2 5h20v14H2z M4 7v.4l8 5 8-5V7l-8 5z" fill-rule="evenodd"/></svg>
    </li>
  </ul>

  <address class="address">N. 40 Ridge Avenue,<br>Suite 210, Aldermoor, WA 55510</address>
</section>

<section class="card card--back" aria-label="Business card back">
  <div class="brand">
    <span class="brand__dot"></span>
    <span>Dig Line<span class="brand__sub">Contracting Inc</span></span>
  </div>
</section>

</body>
</html>
```